Expensive Jewelery and Gold Website

I require a one page template design for my site PrimeIngotHouse.net. We sell replica gold bars. Not real ones, they are novelty gifts.

I have several images of the bars (attached)
I would like a stylish and professional template layout that will be used on my site.

Designed to appear to businesses and professionals and not the members of the public.

There is no idenity or artwork for the business so you may use whichever scheme you wish to. But must somehow stylish use the images or 2-3 of the images attached.

Target Market(s)

Business and marketing professional.

Industry/Entity Type

Business

Requirements
Must have
• Incorporate some or all of images
Nice to have
• Colour/styled images to match design and look in-keeping

```html
<!DOCTYPE html>
<html lang="en">
<head>
<meta charset="utf-8">
<title>PrimeIngotHouse – Replica Gold Bars</title>
<link rel="stylesheet" href="https://fonts.googleapis.com/css2?family=PT+Sans:ital,wght@0,400;0,700;1,400;1,700&family=Arimo:wght@400&display=swap">
<style>
  :root {
    --night: #05080c;
    --glow: #a88a34;
    --gold: #f2b81e;
    --gold-deep: #d99b0c;
    --bar-top: #4a4a4a;
    --bar-bottom: #262626;
    --paper: #e3e3e3;
    --ink: #3a3a3a;
    --ink-soft: #555;
    --light: #dcdcdc;
  }
  * { box-sizing: border-box; margin: 0; padding: 0; }
  html, body { width: 1200px; height: 866px; overflow: hidden; }
  body {
    position: relative;
    background: var(--paper);
    font-family: "Arimo", Arial, sans-serif;
    color: var(--ink);
  }
  .masthead {
    position: absolute; left: 0; top: 0; width: 1200px; height: 480px;
    background:
      radial-gradient(ellipse 560px 330px at 600px 190px, #b99a42 0%, #7a6222 35%, #2a2412 70%, var(--night) 100%);
    border-bottom: 2px solid #d8d2c2;
  }
  .brand {
    position: absolute; left: 160px; top: 18px;
    font-family: "PT Sans", sans-serif; font-weight: 700;
    font-size: 34px; color: #f4f4f4; letter-spacing: -0.5px;
  }
  .tagline {
    position: absolute; left: 160px; top: 57px;
    font-family: "PT Sans", sans-serif; font-style: italic;
    font-size: 13px; color: #f0f0f0;
  }
  .account-links {
    position: absolute; right: 159px; top: 27px;
    font-size: 12px; color: #e6e6e6; word-spacing: 1px;
  }
  .account-links span { margin: 0 4px; }
  .main-nav {
    position: absolute; left: 150px; top: 99px; width: 900px; height: 49px;
    background: linear-gradient(var(--bar-top), var(--bar-bottom));
    border-radius: 12px 12px 0 0;
  }
  .main-nav a {
    position: absolute; top: 0; height: 49px; line-height: 52px;
    font-family: "PT Sans", sans-serif; font-style: italic;
    font-size: 15px; color: #f2f2f2; text-decoration: none;
  }
  .main-nav a.current {
    background: linear-gradient(#f6c636, var(--gold-deep));
    color: #1c1c1c; padding: 0 8px;
  }
  .search {
    position: absolute; left: 716px; top: 15px; width: 167px; height: 21px;
    border-radius: 11px; background: #555; overflow: hidden;
    box-shadow: inset 0 1px 2px #222;
  }
  .search .go {
    position: absolute; right: 0; top: 0; width: 41px; height: 21px;
    background: linear-gradient(#e2e2e2, #a9a9a9);
  }
  .products { position: absolute; left: 150px; top: 148px; width: 900px; height: 332px; display: flex; }
  .product { position: relative; width: 225px; height: 332px; border-right: 1px solid #3c3c3c; }
  .product:last-child { border-right: 0; }
  .product .shot { height: 246px; }
  .shot.gift { background: radial-gradient(circle at 45% 45%, #d7d6dc, #9f9ea4 70%, #6e6b6c); }
  .shot.case-a { background: radial-gradient(circle at 50% 45%, #6a3c1c, #3b1c0b 55%, #c9b39a); }
  .shot.case-b { background: radial-gradient(circle at 50% 50%, #c99438 0%, #1a1614 35%, #7a4a22 75%, #e8e2d6); }
  .shot.case-c { background: radial-gradient(circle at 50% 45%, #5a2c12, #2b1407 55%, #a7998a); }
  .product .caption {
    height: 86px; padding: 11px 0 0 14px;
    background: linear-gradient(#555, #2a2a2a 60%, #1b1b1b);
  }
  .caption h3 {
    font-family: "PT Sans", sans-serif; font-weight: 400;
    font-size: 18px; color: #e4e4e4; line-height: 22px;
  }
  .caption p { font-size: 12px; color: #e0e0e0; margin-top: 1px; }
  .read-more {
    position: absolute; right: 16px; bottom: 11px; width: 81px; height: 23px;
    border-radius: 12px; background: linear-gradient(#fafafa, #b6b6b6);
    font-family: "PT Sans", sans-serif; font-size: 14px; color: #222;
    text-align: center; line-height: 23px; letter-spacing: -0.3px;
  }
  .welcome {
    position: absolute; left: 152px; top: 506px;
    font-family: "PT Sans", sans-serif; font-weight: 700; font-style: italic;
    font-size: 33px; color: #474747; letter-spacing: -1.5px;
  }
  .team-frame {
    position: absolute; left: 155px; top: 556px; width: 232px; height: 192px;
    background: #fff; transform: rotate(2deg); box-shadow: 0 1px 3px #999;
  }
  .team-frame.front { transform: none; left: 158px; top: 561px; width: 228px; height: 183px; padding: 4px; }
  .team-frame .team {
    width: 100%; height: 100%;
    background: linear-gradient(100deg, #3a2f2b, #6b5a50 40%, #4f5560 70%, #d8d8da);
  }
  .intro {
    position: absolute; left: 401px; top: 563px; width: 402px;
    font-size: 12px; line-height: 15.6px; color: #333; letter-spacing: 0.05px;
  }
  .intro p + p { margin-top: 15px; }
  .promo { position: absolute; left: 825px; top: 496px; width: 225px; height: 141px; border: 2px solid #2b2b2b; }
  .promo .top { height: 81px; background: linear-gradient(#3c3c3c, #222); padding: 6px 0 0 14px; color: #e8e8e8; font-family: "PT Sans", sans-serif; }
  .promo .l1 { font-size: 28px; font-weight: 700; line-height: 26px; }
  .promo .l2 { font-size: 21px; font-weight: 700; font-style: italic; line-height: 22px; }
  .promo .l3 { font-size: 14px; line-height: 17px; padding-left: 3px; }
  .promo .bottom { height: 56px; background: linear-gradient(#f7c535, var(--gold-deep)); padding: 3px 0 0 14px; color: #1e1a10; font-family: "PT Sans", sans-serif; font-weight: 700; }
  .promo .b1 { font-size: 16px; line-height: 17px; }
  .promo .b2 { font-size: 21px; line-height: 19px; }
  .promo .b3 { font-size: 12px; line-height: 15px; padding-left: 2px; }
  .footer-rule { position: absolute; left: 150px; top: 778px; width: 900px; border-top: 1px solid #cfcfcf; }
  .footer-nav { position: absolute; left: 150px; top: 794px; font-size: 12px; color: #333; }
  .footer-nav span { margin: 0 7px; }
  .copyright { position: absolute; right: 150px; top: 794px; font-size: 12px; color: #333; }
</style>
</head>
<body>
  <header class="masthead">
    <div class="brand">PrimeIngotHouse</div>
    <div class="tagline">The Best Choice on The Web</div>
    <div class="account-links">My Account<span>|</span>My Wishlist<span>|</span>My Cart<span>|</span>Checkout<span>|</span>Log In</div>

    <nav class="main-nav">
      <a style="left:25px">Home</a>
      <a style="left:80px">About Us</a>
      <a class="current" style="left:146px">Our Products</a>
      <a style="left:251px">Support</a>
      <a style="left:318px">Testimonials</a>
      <a style="left:410px">Contact Us</a>
      <div class="search">
        <div class="go">
          <svg width="41" height="21" viewBox="0 0 41 21"><circle cx="19" cy="9.5" r="5" fill="none" stroke="#222" stroke-width="2"/><line x1="23" y1="13" x2="27" y2="16" stroke="#222" stroke-width="2.4" stroke-linecap="round"/></svg>
        </div>
      </div>
    </nav>

    <section class="products">
      <article class="product">
        <div class="shot gift" role="img" aria-label="Gift-wrapped silver box with organza bow"></div>
        <div class="caption"><h3>Replica gold bar product</h3><p>All products</p></div>
        <div class="read-more">read more</div>
      </article>
      <article class="product">
        <div class="shot case-a" role="img" aria-label="Replica gold bar in open wooden presentation case"></div>
        <div class="caption"><h3>Replica gold bar product</h3><p>All products</p></div>
        <div class="read-more">read more</div>
      </article>
      <article class="product">
        <div class="shot case-b" role="img" aria-label="Close-up of replica gold bar on black velvet in wooden case"></div>
        <div class="caption"><h3>Replica gold bar product</h3><p>All products</p></div>
        <div class="read-more">read more</div>
      </article>
      <article class="product">
        <div class="shot case-c" role="img" aria-label="Stack of wooden presentation cases with replica gold bar"></div>
        <div class="caption"><h3>Replica gold bar product</h3><p>All products</p></div>
        <div class="read-more">read more</div>
      </article>
    </section>
  </header>

  <h1 class="welcome">Welcome to PrimeIngotHouse</h1>
  <div class="team-frame"></div>
  <div class="team-frame front"><div class="team" role="img" aria-label="Group of business professionals"></div></div>

  <div class="intro">
    <p>Lorem ipsum dolor sit amet, consectetur adipisicing elit, sed do eius-mod tempor incididunt ut labore et dolore magna aliqua. Ut enim ad minim veniam, quis nostrud exercitation ullamco laboris nisi ut aliquip ex ea commodo consequat. Duis aute irure dolor in reprehenderit in voluptate velit esse cillum dolore eu fugiat nulla pariatur.</p>
    <p>Lorem ipsum dolor sit amet, consectetur adipisicing elit, sed do eius-mod tempor incididunt ut labore et dolore magna aliqua. Ut enim ad minim veniam, quis nostrud exercitation ullamco laboris nisi ut aliquip ex ea commodo consequat. Duis aute irure dolor in reprehenderit in voluptate velit esse cillum dolore eu fugiat nulla pariatur.Lorem ipsum dolor sit amet, consectetur adipisicing elit.</p>
  </div>

  <aside class="promo">
    <div class="top">
      <div class="l1">REPLICA</div>
      <div class="l2">GOLD BARS</div>
      <div class="l3">At refreshing low price</div>
    </div>
    <div class="bottom">
      <div class="b1">MORE THAN</div>
      <div class="b2">1 MILLION</div>
      <div class="b3">REPLACEMENT PARTS IN STOCK</div>
    </div>
  </aside>

  <div class="footer-rule"></div>
  <footer>
    <div class="footer-nav">Home<span>|</span>About Us<span>|</span>Our Products<span>&nbsp;|</span>Support<span>|</span>Testimonials<span>|</span>Contact Us</div>
    <div class="copyright">Copyright © 2010 PrimeIngotHouse.net . All Rights Reserved.</div>
  </footer>
</body>
</html>
```